Webbanner-Design für Online Druckerei
Zielgruppe
Wir sind eine online Druckerei druckwelle38.de und benötigen 3 Banner für unsere Startseite.
Aufgabenstellung
Wir benötigen für den Slider 3 Banner in der Größe 1662x580px.
Text Banner1:
Overnight- und Expresslieferung bei vielen Produkten möglich
Alle Preise inclusive Versand
Text Banner2:
Broschüren und Magazine
Viele Formate und Papiersorten stehen zur Auswahl
Drahtbindung
Klammerbindung
Spiralbindung
Klebebindung
Jetzt kostenloses Musterexemplar bestellen LINK: (https://www.druckwelle38.de/muster/broschueren)
Text Banner 3:
Wir sind für Sie da
Hotline 0800-417295
Zahldienstleisterlogos: Vorkasse, Blitzzahlung, Vorkasse, Kartoplex, Zenu
Dieses Bild kann verwendet werden:
https://www.druckwelle38.de/reseller_files/350/771/template/images/header-subpages.png

```html
<!DOCTYPE html>
<html lang="de">
<head>
<meta charset="utf-8">
<title>druckwelle38.de – Startseiten-Banner</title>
<link rel="stylesheet" href="https://fonts.googleapis.com/css2?family=Raleway:wght@300;400;600;700;800&display=swap">
<style>
  :root{
    --stage:#9b9b9b;
    --white:#ffffff;
    --ink:#3a3a3a;
    --nav:#555555;
    --accent:#e4325a;
    --tab-grey:#8e8e8e;
    --tab-dark:#3c3c3c;
    --topbar:#1c1c1c;
    --mint:#dfe9e4;
  }
  *{box-sizing:border-box;margin:0;padding:0}
  html,body{width:896px;height:1200px;overflow:hidden}
  body{background:var(--stage);font-family:'Raleway',sans-serif;position:relative}
  .page{position:absolute;left:58px;width:780px;height:376px;background:var(--white);overflow:hidden}
  .page--delivery{top:18px}
  .page--brochures{top:412px}
  .page--service{top:806px}

  .topbar{height:15px;background:var(--topbar);position:relative}
  .topbar__icons{position:absolute;right:122px;top:5px;display:flex;gap:7px;align-items:center}
  .topbar__icons span{display:block;width:4px;height:5px;background:#d8d8d8;border-radius:1px}
  .topbar__icons i{display:block;width:1px;height:6px;background:#888}

  .site-header{height:53px;position:relative}
  .logo{position:absolute;left:124px;top:17px;font-weight:800;font-size:17px;color:#8d8d8d;letter-spacing:-.2px}
  .main-nav{position:absolute;left:322px;top:21px;display:flex;gap:18px;font-size:8px;color:var(--nav);letter-spacing:.2px}
  .header-search{position:absolute;left:638px;top:21px;display:flex;align-items:center;gap:8px}
  .header-search i{display:block;width:1px;height:9px;background:var(--accent)}

  .banner{position:relative;height:240px;overflow:hidden}
  .banner__photo{position:absolute;inset:0}

  .delivery__icon{position:absolute;left:39px;top:40px}
  .delivery__title{position:absolute;left:39px;top:82px;font-weight:300;font-size:20px;line-height:24px;color:var(--accent);text-transform:uppercase}
  .delivery__sub{position:absolute;left:39px;top:129px;font-weight:300;font-size:20px;line-height:24px;color:var(--white)}
  .delivery__note{position:absolute;left:40px;top:157px;font-weight:700;font-size:9px;color:var(--white)}

  .brochures__text{position:absolute;left:0;right:0;top:68px;text-align:center;color:var(--white)}
  .brochures__title{font-weight:400;font-size:20px;line-height:23px;text-transform:uppercase}
  .brochures__sub{font-weight:300;font-size:20px;line-height:23px}
  .bindings{display:flex;justify-content:center;gap:10px;margin-top:7px;font-weight:700;font-size:9px}
  .bindings li{list-style:none;display:flex;align-items:center;gap:3px}
  .cta{display:inline-block;margin-top:14px;background:var(--accent);color:var(--white);font-size:10px;font-weight:400;padding:5px 8px;border-radius:3px;text-decoration:none}

  .service__hello{position:absolute;left:428px;top:80px;font-weight:300;font-size:20px;color:var(--ink)}
  .service__phone{position:absolute;left:428px;top:104px;font-weight:400;font-size:20px;color:var(--accent);display:flex;align-items:center;gap:4px}
  .payments{position:absolute;left:428px;top:200px;display:flex;align-items:center;gap:16px;font-weight:700;font-size:10px;color:#2b2b3f}

  .offer-tabs{position:absolute;left:123px;top:326px;display:flex}
  .offer-tab{width:178px;height:50px;text-align:center;color:rgba(255,255,255,.75);font-weight:300;font-size:17px;padding-top:8px}
  .offer-tab svg{display:block;margin:3px auto 0}
  .offer-tab--one{background:var(--tab-grey)}
  .offer-tab--two{background:var(--accent)}
  .offer-tab--three{background:var(--tab-dark)}
</style>
</head>
<body>

<section class="page page--delivery">
  <div class="topbar"><div class="topbar__icons"><span></span><i></i><span></span></div></div>
  <header class="site-header">
    <div class="logo">druckwelle38.de</div>
    <nav class="main-nav"><span>HOME</span><span>PRODUKTE</span><span>FAQ</span><span>KONTAKT</span></nav>
    <div class="header-search">
      <svg width="9" height="9" viewBox="0 0 10 10"><circle cx="4" cy="4" r="3" fill="none" stroke="#444" stroke-width="1.4"/><line x1="6.3" y1="6.3" x2="9" y2="9" stroke="#444" stroke-width="1.4"/></svg><i></i>
    </div>
  </header>
  <div class="banner">
    <div class="banner__photo" role="img" aria-label="Lieferwagen auf einer Landstraße im Sonnenuntergang"
      style="background:radial-gradient(ellipse at 48% 20%,#f3c06a 0%,#b47a3c 22%,rgba(110,70,40,0) 55%),linear-gradient(90deg,#3b2a1e 0%,#6d4a2c 45%,#7a5538 70%,#4a3526 100%)"></div>
    <svg class="delivery__icon" width="44" height="30" viewBox="0 0 46 32" fill="none" stroke="#fff" stroke-width="1.6" stroke-linejoin="round">
      <path d="M14 3a9 9 0 1 0 9 11 7 7 0 0 1-9-11z"/>
      <path d="M2 12h26v14H2z"/><path d="M28 16h8l6 6v4H28z"/>
      <circle cx="9" cy="27" r="3" fill="#6d4a2c"/><circle cx="35" cy="27" r="3" fill="#6d4a2c"/>
    </svg>
    <h1 class="delivery__title">Overnight-<br>und Expresslieferung</h1>
    <p class="delivery__sub">bei vielen Produkten möglich</p>
    <p class="delivery__note">Alle Preise inklusive Versand</p>
  </div>
  <div class="offer-tabs">
    <div class="offer-tab offer-tab--one">Angebot #1<svg width="18" height="14" viewBox="0 0 18 14" fill="none" stroke="#fff" stroke-width="1.2"><path d="M1 2l5-1 6 2 5-1v11l-5 1-6-2-5 1z M6 1v11 M12 3v11"/></svg></div>
    <div class="offer-tab offer-tab--two">Angebot #2<svg width="18" height="14" viewBox="0 0 18 14" fill="none" stroke="#fff" stroke-width="1.2"><path d="M1 2l5-1 6 2 5-1v11l-5 1-6-2-5 1z M6 1v11 M12 3v11"/></svg></div>
    <div class="offer-tab offer-tab--three">Angebot #3<svg width="18" height="14" viewBox="0 0 18 14" fill="none" stroke="#fff" stroke-width="1.2"><path d="M1 2l5-1 6 2 5-1v11l-5 1-6-2-5 1z M6 1v11 M12 3v11"/></svg></div>
  </div>
</section>

<section class="page page--brochures">
  <div class="topbar"><div class="topbar__icons"><span></span><i></i><span></span></div></div>
  <header class="site-header">
    <div class="logo">druckwelle38.de</div>
    <nav class="main-nav"><span>HOME</span><span>PRODUKTE</span><span>FAQ</span><span>KONTAKT</span></nav>
    <div class="header-search">
      <svg width="9" height="9" viewBox="0 0 10 10"><circle cx="4" cy="4" r="3" fill="none" stroke="#444" stroke-width="1.4"/><line x1="6.3" y1="6.3" x2="9" y2="9" stroke="#444" stroke-width="1.4"/></svg><i></i>
    </div>
  </header>
  <div class="banner">
    <div class="banner__photo" role="img" aria-label="Aufgefächerte Stapel bunter Magazine und Broschüren"
      style="background:linear-gradient(120deg,#5a3a2c 0%,#3d3733 30%,#4a4f48 55%,#3a3632 75%,#5c4638 100%)"></div>
    <div class="brochures__text">
      <h2 class="brochures__title">Broschüren und Magazine</h2>
      <p class="brochures__sub">Viele Formate und Papiersorten stehen zur Auswahl</p>
      <ul class="bindings">
        <li><svg width="12" height="10" viewBox="0 0 12 10"><path d="M1 5l3.5 3.5L11 1" fill="none" stroke="#e4325a" stroke-width="1.8"/></svg>Drahtbindung</li>
        <li><svg width="12" height="10" viewBox="0 0 12 10"><path d="M1 5l3.5 3.5L11 1" fill="none" stroke="#e4325a" stroke-width="1.8"/></svg>Klammerbindung</li>
        <li><svg width="12" height="10" viewBox="0 0 12 10"><path d="M1 5l3.5 3.5L11 1" fill="none" stroke="#e4325a" stroke-width="1.8"/></svg>Spiralbindung</li>
        <li><svg width="12" height="10" viewBox="0 0 12 10"><path d="M1 5l3.5 3.5L11 1" fill="none" stroke="#e4325a" stroke-width="1.8"/></svg>Klebebindung</li>
      </ul>
      <a class="cta" href="https://www.druckwelle38.de/muster/broschueren">Jetzt kostenloses Musterexemplar bestellen</a>
    </div>
  </div>
  <div class="offer-tabs">
    <div class="offer-tab offer-tab--one">Angebot #1<svg width="18" height="14" viewBox="0 0 18 14" fill="none" stroke="#fff" stroke-width="1.2"><path d="M1 2l5-1 6 2 5-1v11l-5 1-6-2-5 1z M6 1v11 M12 3v11"/></svg></div>
    <div class="offer-tab offer-tab--two">Angebot #2<svg width="18" height="14" viewBox="0 0 18 14" fill="none" stroke="#fff" stroke-width="1.2"><path d="M1 2l5-1 6 2 5-1v11l-5 1-6-2-5 1z M6 1v11 M12 3v11"/></svg></div>
    <div class="offer-tab offer-tab--three">Angebot #3<svg width="18" height="14" viewBox="0 0 18 14" fill="none" stroke="#fff" stroke-width="1.2"><path d="M1 2l5-1 6 2 5-1v11l-5 1-6-2-5 1z M6 1v11 M12 3v11"/></svg></div>
  </div>
</section>

<section class="page page--service">
  <div class="topbar"><div class="topbar__icons"><span></span><i></i><span></span></div></div>
  <header class="site-header">
    <div class="logo">druckwelle38.de</div>
    <nav class="main-nav"><span>HOME</span><span>PRODUKTE</span><span>FAQ</span><span>KONTAKT</span></nav>
    <div class="header-search">
      <svg width="9" height="9" viewBox="0 0 10 10"><circle cx="4" cy="4" r="3" fill="none" stroke="#444" stroke-width="1.4"/><line x1="6.3" y1="6.3" x2="9" y2="9" stroke="#444" stroke-width="1.4"/></svg><i></i>
    </div>
  </header>
  <div class="banner" style="background:linear-gradient(90deg,var(--mint),#eef3ef)">
    <div class="banner__photo" role="img" aria-label="Lächelnde Kundenberaterin mit Headset"
      style="left:42px;right:auto;width:300px;background:linear-gradient(180deg,rgba(214,170,120,.35) 0%,rgba(226,196,170,.45) 50%,rgba(40,40,50,.55) 100%)"></div>
    <p class="service__hello">Wir sind für Sie da</p>
    <p class="service__phone"><svg width="13" height="13" viewBox="0 0 14 14"><path d="M3 1l2.5 3-1.3 1.5a8 8 0 0 0 4.3 4.3L10 8.5l3 2.5-1.5 2C6.5 13 1 7.5 1 2.5z" fill="#e4325a"/></svg>0800 417 295</p>
    <div class="payments">
      <span>VORKASSE</span><span>Blitzzahlung</span><span>Netzkasse</span><span>Kartoplex</span><span>Zenu</span>
    </div>
  </div>
  <div class="offer-tabs">
    <div class="offer-tab offer-tab--one">Angebot #1<svg width="18" height="14" viewBox="0 0 18 14" fill="none" stroke="#fff" stroke-width="1.2"><path d="M1 2l5-1 6 2 5-1v11l-5 1-6-2-5 1z M6 1v11 M12 3v11"/></svg></div>
    <div class="offer-tab offer-tab--two">Angebot #2<svg width="18" height="14" viewBox="0 0 18 14" fill="none" stroke="#fff" stroke-width="1.2"><path d="M1 2l5-1 6 2 5-1v11l-5 1-6-2-5 1z M6 1v11 M12 3v11"/></svg></div>
    <div class="offer-tab offer-tab--three">Angebot #3<svg width="18" height="14" viewBox="0 0 18 14" fill="none" stroke="#fff" stroke-width="1.2"><path d="M1 2l5-1 6 2 5-1v11l-5 1-6-2-5 1z M6 1v11 M12 3v11"/></svg></div>
  </div>
</section>

</body>
</html>
```